Web design required

1-We need a web design for existing company based in New Zealand
2-We build residential house and light commercial
3-We has in-house designer which allow us can provide interior design
4-We modeling project before site construction, which enable both client and construction team to visually analysis whole project,

Target Market(s)

middle class residential house market
Ref: http://www.brambleworthbuilders.co.nz/

Industry/Entity Type

Construction Company

Number of Pages Required

1 page

Font styles to use
Sans Serif
Other font styles liked:
• Such as : Central Gothic or similar which has more design taste

Colors

Designer to choose colors to be used in the design.

Requirements
Must have
• Front sheet, contact information, sample project

```html
<!DOCTYPE html>
<html lang="en">
<head>
<meta charset="utf-8">
<title>Kestrel Homes</title>
<link rel="stylesheet" href="https://fonts.googleapis.com/css2?family=Montserrat:wght@400;500;600;700&family=Mulish:wght@400;600&display=swap">
<style>
:root{
  --blue:#1a4f9c;
  --blue-dark:#0f3a78;
  --ink:#111418;
  --text:#55595f;
  --muted:#8d9197;
  --line:#d9dbde;
  --pale:#f6f6f6;
  --white:#ffffff;
}
*{box-sizing:border-box;margin:0;padding:0}
html,body{width:1200px;height:3607px;overflow:hidden;background:var(--white)}
body{position:relative;font-family:"Mulish",Arial,sans-serif;color:var(--text)}
.abs{position:absolute}

/* header */
.site-header{left:0;top:0;width:1200px;height:62px;background:var(--white);z-index:2}
.brand{display:flex;align-items:center;gap:10px;font-family:"Montserrat",Arial,sans-serif;font-weight:600;font-size:17px;color:var(--blue);letter-spacing:.5px}
.brand-dot{width:26px;height:26px;border-radius:50%;background:var(--blue)}
.site-header .brand{position:absolute;left:84px;top:18px}
.main-nav{position:absolute;top:24px;left:553px;font-family:"Montserrat",Arial,sans-serif;font-size:12.5px;font-weight:600;color:var(--ink);letter-spacing:.6px}
.main-nav span{position:absolute;white-space:nowrap}
.main-nav .active{color:var(--blue);border-bottom:2px solid var(--blue);padding-bottom:6px}
.lang{position:absolute;left:1066px;top:24px;font-size:11px;color:var(--text);font-family:"Montserrat",Arial,sans-serif}

/* hero */
.hero{left:0;top:62px;width:1200px;height:496px;background:linear-gradient(100deg,#0b1b2c 0%,#183650 35%,#4a6a82 55%,#1a2d3e 80%,#0a1724 100%);overflow:hidden}
.hero-title{left:185px;top:180px;font-family:"Montserrat",Arial,sans-serif;font-weight:600;font-size:46px;letter-spacing:9px;color:var(--white);white-space:nowrap}
.hero-button{left:185px;top:258px;width:193px;height:41px;border:2px solid var(--white);color:var(--white);font-family:"Montserrat",Arial,sans-serif;font-size:12px;font-weight:600;letter-spacing:2px;display:flex;align-items:center;justify-content:center;gap:10px}
.hero-side{left:1093px;top:222px;writing-mode:vertical-rl;font-family:"Montserrat",Arial,sans-serif;font-weight:600;font-size:15px;letter-spacing:2px;color:var(--white);white-space:nowrap}
.hero-count{left:84px;top:198px;writing-mode:vertical-rl;transform:rotate(180deg);font-family:"Montserrat",Arial,sans-serif;font-size:18px;font-weight:600;letter-spacing:3px;color:var(--white)}

/* section titles */
.section-title{left:0;width:1200px;text-align:center;font-family:"Montserrat",Arial,sans-serif;font-weight:400;font-size:46px;letter-spacing:3px;color:var(--ink)}
.section-title b{font-weight:700}
.section-lead{left:330px;width:540px;text-align:center;font-size:17px;line-height:25px;color:var(--text)}

/* about */
.about-photo{left:142px;top:671px;width:517px;height:351px;background:linear-gradient(180deg,#cfe0f0 0%,#e7eef4 35%,#5b5f63 60%,#3c4043 100%);box-shadow:0 6px 18px rgba(0,0,0,.18)}
.about-rule{left:589px;top:772px;width:128px;height:1px;background:var(--ink)}
.about-title{left:743px;top:748px;font-family:"Montserrat",Arial,sans-serif;font-size:42px;letter-spacing:2px;color:var(--ink);font-weight:400}
.about-title b{font-weight:700}
.about-text{left:743px;top:812px;width:320px;font-size:17px;line-height:22px;color:var(--text)}
.text-link{font-family:"Montserrat",Arial,sans-serif;font-size:12px;font-weight:700;letter-spacing:2.5px;color:var(--blue);display:flex;align-items:center;gap:10px}
.about-link{left:743px;top:896px}

/* services */
.service-card{top:1275px;width:325px;height:318px}
.service-card.raised{background:var(--white);box-shadow:0 2px 10px rgba(0,0,0,.12)}
.service-photo{width:325px;height:166px}
.service-name{margin:27px 0 0 18px;font-family:"Montserrat",Arial,sans-serif;font-weight:600;font-size:17px;letter-spacing:.5px;color:var(--ink);white-space:nowrap}
.service-card.raised .service-name{color:var(--blue)}
.service-text{margin:13px 18px 0 18px;font-size:13px;line-height:19px;color:var(--text)}

/* projects */
.projects-band{left:0;top:1705px;width:1200px;height:1032px;background:var(--pale)}
.projects-mark{left:599px;top:1705px;width:2px;height:44px;background:var(--ink)}
.project-tile{width:308px;height:330px}
.project-caption{left:447px;top:2225px;width:306px;height:67px;background:var(--white);padding:14px 0 0 22px}
.project-caption h3{font-family:"Montserrat",Arial,sans-serif;font-size:14px;font-weight:700;color:var(--blue);letter-spacing:.5px}
.project-caption p{font-size:11px;color:var(--muted);margin-top:5px}

/* contact */
.info-col{left:87px;top:2826px;width:220px}
.info-col h4{font-family:"Montserrat",Arial,sans-serif;font-size:16px;font-weight:700;color:var(--ink);letter-spacing:.5px}
.info-col p{font-size:13px;line-height:19px;color:var(--text);margin-top:8px}
.info-col .mail{color:var(--blue)}
.quote{left:87px;top:3082px;display:flex;align-items:center;gap:14px}
.quote small{display:block;font-family:"Montserrat",Arial,sans-serif;font-size:10px;font-weight:700;color:var(--ink);letter-spacing:.5px}
.quote strong{display:block;font-family:"Montserrat",Arial,sans-serif;font-size:19px;font-weight:700;color:var(--ink);letter-spacing:.5px}
.field{left:337px;width:411px;border:1px solid var(--line);background:var(--white);font-size:11px;letter-spacing:1px;color:#a5a8ad;padding:16px 0 0 15px}
.send{left:337px;top:3189px;width:238px;height:53px;background:var(--blue);color:var(--white);font-family:"Montserrat",Arial,sans-serif;font-size:15px;font-weight:600;letter-spacing:1px;display:flex;align-items:center;justify-content:center}
.office-card{left:786px;top:2768px;width:325px;height:474px;background:var(--white);box-shadow:0 2px 12px rgba(0,0,0,.13)}
.office-map{width:325px;height:274px;background:linear-gradient(135deg,#eef0ea 0%,#e3e6dd 50%,#f1ead0 100%)}
.office-card h4{margin:40px 0 0 33px;font-family:"Montserrat",Arial,sans-serif;font-size:17px;font-weight:700;color:var(--blue-dark);letter-spacing:.5px}
.office-list{list-style:none;margin:20px 33px 0 33px;font-size:12.5px;line-height:18px;color:var(--text)}
.office-list li{display:flex;gap:14px;margin-bottom:10px}
.office-list svg{flex:none;margin-top:2px}

/* footer */
.site-footer .brand{position:absolute;left:518px;top:3370px}
.footer-nav{left:0;top:3437px;width:1200px;display:flex;justify-content:center;gap:40px;font-family:"Montserrat",Arial,sans-serif;font-size:13px;font-weight:600;letter-spacing:.8px;color:var(--ink)}
.footer-nav .active{color:var(--blue)}
.social{top:3485px;width:27px;height:27px;border:1.5px solid #b7bbc0;border-radius:50%}
.copyright{left:0;top:3536px;width:1200px;text-align:center;font-size:11px;color:var(--muted)}
</style>
</head>
<body>

<header class="site-header abs">
  <div class="brand"><span class="brand-dot"></span>KESTREL HOMES</div>
  <nav class="main-nav">
    <span class="active" style="left:0">HOME</span>
    <span style="left:78px">ABOUT</span>
    <span style="left:164px">SERVICES</span>
    <span style="left:267px">PROJECTS</span>
    <span style="left:375px">CONTACT US</span>
  </nav>
  <div class="lang">◯ &nbsp;EN ▾</div>
</header>

<section class="hero abs" role="img" aria-label="Night photograph of a waterfront home with lit terrace and harbour lights"></section>
<div class="hero-count abs">01</div>
<svg class="abs" style="left:92px;top:245px" width="12" height="270" viewBox="0 0 12 270" aria-hidden="true">
  <circle cx="6" cy="6" r="2" fill="#fff"/><circle cx="6" cy="40" r="2" fill="#fff"/>
  <rect x="1" y="80" width="10" height="16" rx="5" fill="none" stroke="#fff" stroke-width="1.5"/>
  <line x1="6" y1="110" x2="6" y2="270" stroke="#fff" stroke-width="1"/>
</svg>
<h1 class="hero-title abs">KESTREL HOMES</h1>
<div class="hero-button abs">LEARN MORE
  <svg width="22" height="8" viewBox="0 0 22 8" aria-hidden="true"><path d="M0 4H20M16 1L20 4L16 7" fill="none" stroke="#fff" stroke-width="1.3"/></svg>
</div>
<div class="hero-side abs">INTERIOR DESIGN</div>

<section class="about">
  <div class="about-photo abs" role="img" aria-label="House under construction wrapped in scaffolding"></div>
  <div class="about-rule abs"></div>
  <h2 class="about-title abs"><b>ABOUT</b> US</h2>
  <p class="about-text abs">Kestrel Homes is dedicated to creating and renovating beautiful and unusual buildings.</p>
  <div class="text-link about-link abs">LEARN MORE
    <svg width="34" height="8" viewBox="0 0 34 8" aria-hidden="true"><path d="M0 4H32M28 1L32 4L28 7" fill="none" stroke="#1a4f9c" stroke-width="1.3"/></svg>
  </div>
</section>

<section class="services">
  <h2 class="section-title abs" style="top:1122px">OUR <b>SERVICES</b></h2>
  <p class="section-lead abs" style="top:1183px">Kestrel Homes works with you to take dream houses off the blue-prints and into reality.</p>

  <article class="service-card abs" style="left:84px">
    <div class="service-photo" role="img" aria-label="Hands sketching plans over printed drawings" style="background:linear-gradient(135deg,#c9b9ae,#e8e4df 55%,#8c7a70)"></div>
    <h3 class="service-name">PRECONSTRUCTION PLANNING</h3>
    <p class="service-text">This is a short sample note for this service. gravida nibh vel velit auctor aliquet. Aenean sollicitudin, lorem quis bibendum auctor,</p>
  </article>
  <article class="service-card raised abs" style="left:438px">
    <div class="service-photo" role="img" aria-label="Builders working on a site seen from above" style="background:linear-gradient(135deg,#b38a4a,#6d5a3e 50%,#c99c58)"></div>
    <h3 class="service-name">CONSTRUCTION MODELLING</h3>
    <p class="service-text">This is a short sample note for this service. gravida nibh vel velit auctor aliquet. Aenean sollicitudin, lorem quis bibendum auctor,</p>
  </article>
  <article class="service-card abs" style="left:789px">
    <div class="service-photo" role="img" aria-label="White two-storey house with verandas under blue sky" style="background:linear-gradient(180deg,#5f86c4,#b6c6dc 55%,#e9ebea)"></div>
    <h3 class="service-name">FULL PROJECT MANAGEMENT</h3>
    <p class="service-text">This is a short sample note for this service. gravida nibh vel velit auctor aliquet. Aenean sollicitudin, lorem quis bibendum auctor,</p>
  </article>
</section>

<section class="projects">
  <div class="projects-band abs"></div>
  <div class="projects-mark abs"></div>
  <h2 class="section-title abs" style="top:1781px">OUR <b>PROJECTS</b></h2>
  <p class="section-lead abs" style="top:1845px">Kestrel Homes works with you to take dream houses off the blue-prints and into reality.</p>

  <div class="project-tile abs" style="left:113px;top:1962px;background:linear-gradient(135deg,#9a7a4e,#d9d4cb 50%,#4e5660)" role="img" aria-label="Team reviewing plans around a table"></div>
  <div class="project-tile abs" style="left:447px;top:1962px;height:263px;width:306px;background:linear-gradient(180deg,#2a4f8f,#1c3f7c)" role="img" aria-label="Suburban house with blue overlay"></div>
  <svg class="abs" style="left:578px;top:2071px" width="44" height="44" viewBox="0 0 44 44" aria-hidden="true">
    <circle cx="22" cy="22" r="20" fill="none" stroke="#fff" stroke-width="1.5"/>
    <path d="M22 12V32M12 22H32" stroke="#fff" stroke-width="1.5"/>
  </svg>
  <div class="project-caption abs"><h3>HARBOURVIEW PROJECT</h3><p>Kestrel Homes Is Dedicated to Creating</p></div>
  <div class="project-tile abs" style="left:779px;top:1962px;background:linear-gradient(135deg,#3a3d44,#8e9096 55%,#3c3f46)" role="img" aria-label="Hand holding an architectural drawing"></div>

  <div class="project-tile abs" style="left:113px;top:2321px;background:linear-gradient(180deg,#3b3b3b,#bdbdbd 55%,#2c2c2c)" role="img" aria-label="Hanging light bulbs in black and white"></div>
  <div class="project-tile abs" style="left:447px;top:2321px;width:306px;background:linear-gradient(180deg,#eceae6,#d6cfc6 60%,#b58d5f)" role="img" aria-label="Bright living room with timber floor"></div>
  <div class="project-tile abs" style="left:779px;top:2321px;background:linear-gradient(180deg,#c0622f,#7d8a8c 45%,#3c4a4c)" role="img" aria-label="Glazed café interior with orange pendant lamps"></div>
</section>

<section class="contact">
  <div class="info-col abs">
    <h4>INQUIRIES</h4>
    <p>For any inquiries, questions or commendations, please call or fill out the following form</p>
    <h4 style="margin-top:26px">EMPLOYMENT</h4>
    <p>To apply for a job with Kestrel Homes, please send a cover letter together with your C.V. to: <span class="mail">info@kestrelhomes.co.nz</span></p>
  </div>
  <div class="quote abs">
    <svg width="36" height="36" viewBox="0 0 24 24" aria-hidden="true"><path d="M6.6 10.8a15 15 0 0 0 6.6 6.6l2.2-2.2c.3-.3.7-.4 1-.2 1.1.4 2.3.6 3.6.6.6 0 1 .4 1 1V20c0 .6-.4 1-1 1A17 17 0 0 1 3 4c0-.6.4-1 1-1h3.5c.6 0 1 .4 1 1 0 1.3.2 2.5.6 3.6.1.3 0 .7-.2 1z" fill="none" stroke="#111418" stroke-width="1.4"/></svg>
    <div><small>GET A QUOTE:</small><strong>09 487 2210</strong></div>
  </div>

  <div class="field abs" style="top:2835px;height:51px">FULL NAME</div>
  <div class="field abs" style="top:2905px;height:51px">EMAIL</div>
  <div class="field abs" style="top:2975px;height:192px">MESSAGE</div>
  <div class="send abs">SEND NOW</div>

  <div class="office-card abs">
    <div class="office-map" role="img" aria-label="Street map around the head office with a location pin"></div>
    <h4>HEAD OFFICE</h4>
    <ul class="office-list">
      <li><svg width="10" height="14" viewBox="0 0 10 14" aria-hidden="true"><path d="M5 0a5 5 0 0 1 5 5c0 3.5-5 9-5 9S0 8.5 0 5a5 5 0 0 1 5-5z" fill="#111418"/><circle cx="5" cy="5" r="1.8" fill="#fff"/></svg>17 Harrowfield Lane, Flat Bush Auckland</li>
      <li><svg width="10" height="14" viewBox="0 0 10 14" aria-hidden="true"><rect x="1" y="0.5" width="8" height="13" rx="1.5" fill="#111418"/><rect x="2.5" y="2" width="5" height="8" fill="#fff"/></svg>0064 9 487 2210</li>
      <li><svg width="12" height="10" viewBox="0 0 12 10" aria-hidden="true"><rect x="0" y="1" width="12" height="8" fill="#111418"/><path d="M0.5 1.5L6 5.5L11.5 1.5" fill="none" stroke="#fff" stroke-width="1"/></svg>info@kestrelhomes.co.nz</li>
    </ul>
  </div>
  <svg class="abs" style="left:931px;top:2918px" width="34" height="48" viewBox="0 0 34 48" aria-hidden="true">
    <path d="M17 0a17 17 0 0 1 17 17c0 12-17 31-17 31S0 29 0 17A17 17 0 0 1 17 0z" fill="#0f3a78"/>
    <circle cx="17" cy="17" r="6" fill="#fff"/>
  </svg>
</section>

<footer class="site-footer">
  <div class="brand"><span class="brand-dot"></span>KESTREL HOMES</div>
  <nav class="footer-nav abs"><span class="active">HOME</span><span>ABOUT</span><span>SERVICES</span><span>PROJECTS</span><span>CONTACT US</span></nav>
  <span class="social abs" style="left:531px"></span>
  <span class="social abs" style="left:587px"></span>
  <span class="social abs" style="left:642px"></span>
  <p class="copyright abs">© 2017 by Kestrel Homes</p>
</footer>

</body>
</html>
```